Brimvane.com fiber optic internet website redesign

We need a new website design for our fiber optic internet company that provides internet, phone, and tv services. It should use the text "Marrowfen fiber optics", and "I beamed up with Marrowfen". The design should use the color blue and the attached logo.
We are a 30 year old internet company who started as a dial up internet provider in our basement. Today we design, build, and maintain our own fiber optic internet network to provide service to residential, business, educational, healthcare, and governmental customers

```html
<!DOCTYPE html>
<html lang="en">
<head>
<meta charset="utf-8">
<title>Virtual Hosting – Brimvane.com</title>
<link rel="stylesheet" href="https://fonts.googleapis.com/css2?family=Poppins:wght@400;500;600&family=Roboto+Condensed:wght@700&display=swap">
<style>
:root{
  --blue:#1f6fdc;
  --blue-deep:#0d4aa6;
  --navy:#2b4f8f;
  --ink:#333a44;
  --teal:#0f5b6e;
  --pale:#eef5fd;
  --foot:#e9f1fc;
  --row:#dbe8fa;
  --bar:#a9c0e0;
  --white:#ffffff;
}
*{box-sizing:border-box;margin:0;padding:0}
html,body{width:1200px;height:2626px;overflow:hidden}
body{font-family:"Poppins",sans-serif;background:var(--white);position:relative;color:var(--ink)}
.abs{position:absolute}

/* hero */
.hero{left:0;top:0;width:1200px;height:670px;overflow:hidden}
.hero-photo{left:0;top:0;width:1200px;height:640px;background:radial-gradient(ellipse at 55% 35%,#5b7fc0 0%,#2d55a0 45%,#173a80 100%)}
.hero-wave{left:0;top:460px;width:1200px;height:210px}
.brand{display:flex;align-items:center;gap:12px;color:var(--white);white-space:nowrap}
.brand-dot{width:46px;height:46px;border-radius:50%;background:var(--white);flex:none}
.brand-name{font-size:23px;font-weight:600;line-height:1;display:block}
.brand-sub{font-size:10px;font-weight:500;display:block;margin-top:3px}
.nav-brand{left:135px;top:31px}
.menu{left:387px;top:45px;display:flex;gap:18px;font-size:14px;font-weight:500;color:var(--white);white-space:nowrap}
.call{left:940px;top:38px;width:148px;height:34px;background:var(--blue);color:var(--white);border-radius:18px;font-size:12px;display:flex;align-items:center;justify-content:center;gap:8px;white-space:nowrap}
.hero-title{left:0;top:236px;width:1200px;text-align:center;font-family:"Roboto Condensed",sans-serif;font-weight:700;font-size:50px;color:var(--white)}

/* pricing table */
.pricing{left:180px;top:745px;display:flex;box-shadow:0 4px 14px rgba(0,40,100,.12);border-radius:8px}
.col{width:167px;display:flex;flex-direction:column}
.col-head{height:100px;display:flex;justify-content:center;padding-top:24px;font-family:"Roboto Condensed",sans-serif;font-weight:700;font-size:20px;color:var(--white);clip-path:polygon(0 0,100% 0,100% 65%,50% 100%,0 65%);border-radius:8px 8px 0 0;white-space:nowrap}
.col-pkg .col-head{background:#e8f0fb;color:var(--blue-deep);clip-path:none;padding-top:28px}
.cell{height:53px;display:flex;align-items:center;justify-content:center;font-size:13px;font-weight:500;color:#111}
.col-pkg .cell{font-size:18px;font-weight:400;color:var(--ink);background:#eef3fb}
.cell:nth-child(2),.cell:nth-child(4),.col-pkg .cell:nth-child(2),.col-pkg .cell:nth-child(4){background:var(--row)}
.h1{background:var(--navy)}.h2{background:#2f5da8}.h3{background:#2867c4}.h4{background:#2a79e0}

/* access feature */
.feature{left:0;top:1105px;width:1200px;height:705px;background:var(--pale)}
.frame-top{left:469px;top:1216px;width:177px;height:176px;border:12px solid var(--blue);border-bottom:none;border-left:none;border-radius:0 16px 0 0}
.frame-bot{left:180px;top:1546px;width:176px;height:176px;border:12px solid var(--blue);border-top:none;border-right:none;border-radius:0 0 0 16px}
.feature-photo{left:191px;top:1228px;width:444px;height:483px;border-radius:18px;background:linear-gradient(135deg,#7fa9c9 0%,#3a6a95 45%,#0f2745 100%)}
.feature-title{left:690px;top:1386px;width:360px;font-family:"Roboto Condensed",sans-serif;font-weight:700;font-size:38px;line-height:57px;color:var(--ink)}
.btn{border-radius:18px;font-size:13px;display:flex;align-items:center;justify-content:center;white-space:nowrap}
.btn-solid{left:687px;top:1520px;width:168px;height:36px;background:var(--blue);color:var(--white)}

/* voip band */
.voip{left:0;top:1810px;width:1196px;height:440px;background:radial-gradient(ellipse at 30% 40%,#0c3a52 0%,#06121f 60%,#030a14 100%);overflow:hidden}
.voip-title{left:0;top:1900px;width:1200px;text-align:center;font-family:"Roboto Condensed",sans-serif;font-weight:700;font-size:38px;line-height:47px;color:var(--white)}
.btn-line{left:517px;top:2010px;width:167px;height:34px;border:1.5px solid var(--white);color:var(--white)}
.voip-wave{left:0;top:2060px;width:1200px;height:200px}

/* footer */
.footer{left:0;top:2250px;width:1200px;height:330px;background:var(--foot)}
.foot-brand{left:163px;top:2320px;color:#111}
.foot-brand .brand-dot{background:var(--blue-deep)}
.foot-about{left:157px;top:2398px;width:305px;font-size:15px;line-height:23px;color:#444}
.foot-head{font-size:17px;font-weight:600;color:var(--teal)}
.links{left:553px;top:2293px}
.links ul{list-style:none;margin-top:30px}
.links li{font-size:15px;color:#444;margin-bottom:15px}
.contact{left:795px;top:2293px}
.contact-row{display:flex;align-items:center;gap:18px;font-size:15px;color:#444;margin-top:28px}
.contact-row + .contact-row{margin-top:24px}
.icon-box{width:38px;height:38px;border:1.5px solid #b9cbe6;border-radius:8px;display:flex;align-items:center;justify-content:center;background:var(--white)}
.socials{display:flex;gap:22px;margin-top:28px;margin-left:3px}
.social{width:34px;height:34px;border-radius:50%;background:var(--blue)}
.copy{left:0;top:2580px;width:1200px;height:46px;background:var(--bar);color:var(--white);font-size:15px;display:flex;align-items:center;justify-content:center}
</style>
</head>
<body>

<section class="abs hero">
  <div class="abs hero-photo" role="img" aria-label="Hands touching a glowing grid of floating video screens"></div>
  <svg class="abs hero-wave" viewBox="0 0 1200 210" preserveAspectRatio="none">
    <path d="M0 150 C90 210 160 190 240 110 C330 20 380 0 470 50 C560 110 600 170 690 140 C780 110 830 40 960 60 C1060 80 1120 140 1200 95 L1200 210 L0 210 Z" fill="#0d4aa6"/>
    <path d="M0 175 C90 200 160 170 250 110 C330 60 400 40 480 95 C560 150 610 185 690 158 C790 120 850 80 970 100 C1070 116 1130 150 1200 125 L1200 210 L0 210 Z" fill="#ffffff"/>
  </svg>
  <div class="abs brand nav-brand"><span class="brand-dot"></span><span><span class="brand-name">Brimvane.com</span><span class="brand-sub">Marrowfen fiber optics</span></span></div>
  <nav class="abs menu"><span>Home</span><span>Residential</span><span>Business</span><span>Services</span><span>Telecom</span><span>Contact us</span><span>Users</span></nav>
  <div class="abs call"><svg width="11" height="11" viewBox="0 0 24 24"><path fill="#fff" d="M6.6 10.8a15 15 0 006.6 6.6l2.2-2.2a1 1 0 011-.25 11.4 11.4 0 003.6.57 1 1 0 011 1V20a1 1 0 01-1 1A17 17 0 013 4a1 1 0 011-1h3.5a1 1 0 011 1c0 1.25.2 2.45.57 3.6a1 1 0 01-.25 1z"/></svg>1-888-555-0142</div>
  <h1 class="abs hero-title">Virtual Hosting</h1>
</section>

<div class="abs pricing">
  <div class="col col-pkg"><div class="col-head">Package</div><div class="cell">Basic</div><div class="cell">E-Commerce</div><div class="cell">Advanced</div></div>
  <div class="col"><div class="col-head h1">Disk Space</div><div class="cell">250MB</div><div class="cell">500MB</div><div class="cell">1000MB</div></div>
  <div class="col"><div class="col-head h2">Transfer</div><div class="cell">25GB</div><div class="cell">50GB</div><div class="cell">100GB</div></div>
  <div class="col"><div class="col-head h3">Email Boxes</div><div class="cell">25</div><div class="cell">50</div><div class="cell">100</div></div>
  <div class="col"><div class="col-head h4">Monthly Price</div><div class="cell">$15</div><div class="cell">$30</div><div class="cell">$50</div></div>
</div>

<section class="abs feature"></section>
<div class="abs frame-top"></div>
<div class="abs frame-bot"></div>
<div class="abs feature-photo" role="img" aria-label="Hand pressing a glowing file transfer gear symbol"></div>
<h2 class="abs feature-title">Hostdeck or FTP Access to *nix Server</h2>
<div class="abs btn btn-solid">Check Availability</div>

<section class="abs voip" role="img" aria-label="Dark background with flowing teal network lines"></section>
<h2 class="abs voip-title">Add VoIP Phone Service for $25/mo OR<br>Bundle with Internet + TV for $15/mo</h2>
<div class="abs btn btn-line">Check Availability</div>
<svg class="abs voip-wave" viewBox="0 0 1200 200" preserveAspectRatio="none">
  <path d="M0 50 C60 10 110 20 170 60 C250 120 290 200 380 170 C470 140 520 50 610 45 C700 40 750 120 850 125 C950 130 1060 30 1200 100 L1200 200 L0 200 Z" fill="#2a7fe6"/>
  <path d="M0 85 C70 60 130 80 190 120 C260 170 310 210 400 180 C480 150 530 90 620 85 C710 80 760 140 850 140 C950 140 1070 75 1200 135 L1200 200 L0 200 Z" fill="#e9f1fc"/>
</svg>

<footer class="abs footer"></footer>
<div class="abs brand foot-brand"><span class="brand-dot"></span><span><span class="brand-name">Brimvane.com</span><span class="brand-sub">Marrowfen fiber optics</span></span></div>
<p class="abs foot-about">Lorem ipsum dolor sit amet, consectetur adipiscing elit, sed do eiusmod tempor incididunt ut labore et dolore magna aliqua. Ut enim ad minim veniam, quis nostrud</p>
<div class="abs links">
  <div class="foot-head">Quick Links</div>
  <ul><li>Home</li><li>Services</li><li>Our Work</li><li>About us</li><li>Contact Us</li></ul>
</div>
<div class="abs contact">
  <div class="foot-head">Contact Info</div>
  <div class="contact-row"><span class="icon-box"><svg width="14" height="14" viewBox="0 0 24 24"><path fill="#1f6fdc" d="M6.6 10.8a15 15 0 006.6 6.6l2.2-2.2a1 1 0 011-.25 11.4 11.4 0 003.6.57 1 1 0 011 1V20a1 1 0 01-1 1A17 17 0 013 4a1 1 0 011-1h3.5a1 1 0 011 1c0 1.25.2 2.45.57 3.6a1 1 0 01-.25 1z"/></svg></span>1-888-555-0142</div>
  <div class="contact-row"><span class="icon-box"><svg width="14" height="11" viewBox="0 0 24 18"><rect x="1" y="1" width="22" height="16" rx="2" fill="#1f6fdc"/><path d="M2 2l10 8 10-8" stroke="#fff" stroke-width="2" fill="none"/></svg></span>hello@brimvane.com</div>
  <div class="socials"><span class="social"></span><span class="social"></span><span class="social"></span></div>
</div>
<div class="abs copy">Copyright © 2024 Brimvane.com</div>

</body>
</html>
```